Book cover for ebook and Physical book for Mind Clutter Collective

I run a non-profit Mind Clutter Collective and I have a new book that needs a cover. For the physical book, I will need a full wrap. The mission is to help individuals Quiet the cycle of restless worry patterns. This book is title is "Quiet the cycle of restless worry patterns", and subtitle "Clear Your Mind of Static Noise." I am open to anything design wise, nothing is set in stone. Oh, MCC is pending Trademark.

Target Market(s)

Typically it's Mom's from 25-40

Industry/Entity Type

Mental Health

Font styles to use
Serif

Colors
f37122
9bcb3b
fbed22
0255a3
e34197

Requirements
Must have
• I do like simplicity, yet vibrant colors.
Nice to have
• The authors are Rex T. Whitford, and Dana Okonkwo. For some inspiration individuals refer to me as the Wonder Guide having reversed five incurable diseases.
Should not have
• The cover shouldn't be too busy.

```html
<!DOCTYPE html>
<html lang="en">
<head>
<meta charset="utf-8">
<title>Quiet the Cycle of Restless Worry Patterns — Cover</title>
<link rel="stylesheet" href="https://fonts.googleapis.com/css2?family=Oswald:wght@500;700&display=swap">
<style>
  :root {
    --page-bg: #ffffff;
    --sky: #3dbbe8;
    --sky-haze: #43b7c9;
    --meadow-light: #3fae4e;
    --meadow: #2f9a2c;
    --meadow-deep: #2a8a24;
    --title-white: #ffffff;
    --author-tint: #d4eef5;
    --subtitle-olive: #8f9636;
    --subtitle-band: rgba(12, 70, 40, 0.6);
  }
  html, body {
    margin: 0;
    padding: 0;
    width: 1200px;
    height: 1200px;
    overflow: hidden;
    background: var(--page-bg);
  }
  .canvas {
    position: relative;
    width: 1200px;
    height: 1200px;
  }
  .cover {
    position: absolute;
    left: 240px;
    top: 62px;
    width: 720px;
    height: 1076px;
    overflow: hidden;
    box-shadow: 4px 4px 10px rgba(0, 0, 0, 0.25);
  }
  .cover-photo {
    position: absolute;
    inset: 0;
    background:
      radial-gradient(ellipse 60% 18% at 50% 92%, rgba(255, 255, 255, 0.35), transparent 70%),
      linear-gradient(180deg,
        var(--sky) 0%,
        var(--sky-haze) 12%,
        var(--meadow-light) 32%,
        var(--meadow) 60%,
        var(--meadow-deep) 100%);
  }
  .cover-text {
    position: absolute;
    inset: 0;
    display: flex;
    flex-direction: column;
    align-items: center;
    font-family: "Oswald", "Arial Narrow", sans-serif;
    text-transform: uppercase;
  }
  .authors {
    margin: 66px 0 0;
    font-weight: 500;
    font-size: 33px;
    letter-spacing: 0.5px;
    color: var(--author-tint);
    opacity: 0.85;
  }
  .title-stack {
    margin-top: 38px;
    display: flex;
    flex-direction: column;
    align-items: center;
  }
  .title-line {
    display: block;
    font-weight: 700;
    font-size: 104px;
    line-height: 80px;
    height: 80px;
    color: var(--title-white);
    letter-spacing: 0.5px;
    position: relative;
    z-index: 2;
  }
  .subtitle-line {
    display: block;
    font-weight: 500;
    font-size: 60px;
    line-height: 78px;
    height: 78px;
    padding: 0 14px;
    color: var(--subtitle-olive);
    background: var(--subtitle-band);
    position: relative;
    z-index: 1;
  }
</style>
</head>
<body>
  <main class="canvas">
    <section class="cover" aria-label="Front cover">
      <div class="cover-photo" role="img" aria-label="Photograph of a sunny green meadow with white wildflowers under a soft blue sky"></div>
      <div class="cover-text">
        <p class="authors">Rex T. Whitford and Dana Okonkwo</p>
        <h1 class="title-stack">
          <span class="title-line">Quiet</span>
          <span class="subtitle-line">Clear</span>
          <span class="title-line">The Cycle</span>
          <span class="subtitle-line">Your Mind</span>
          <span class="title-line">Of Restless</span>
          <span class="subtitle-line">Of</span>
          <span class="title-line">Worry</span>
          <span class="subtitle-line">Static</span>
          <span class="title-line">Patterns</span>
          <span class="subtitle-line">Noise</span>
        </h1>
      </div>
    </section>
  </main>
</body>
</html>
```